Redesign website

I purchased a business a few months ago and I'm in the process on rebranding everything and creating a new website. I want the new website completely different with 5 pages and nice pictures on every page. Also I want my new logo and colors to included on the site.
Current Site https://www.brindlehoundco.com

Industry/Entity Type

Dog Sitting

Coding

Coded - Design and coding required

Number of Pages Required

5+ page

Requirements
Must have
• I have pictures and a video I can shared to use for the website.
Just as the current site it should have an option to be taken to the site I have to make reservations.
Nice to have
• Would be nice to have social media intergrations

```html
<!DOCTYPE html>
<html lang="en">
<head>
<meta charset="utf-8">
<title>Brindle Hound – Daycare, Boarding &amp; Grooming</title>
<link href="https://fonts.googleapis.com/css2?family=Poppins:wght@300;400;500;600;700&display=swap" rel="stylesheet">
<style>
:root{
  --teal:#1ebcd0;
  --teal-dark:#12a9bd;
  --teal-light:#3ee6d4;
  --magenta:#c8106e;
  --pink:#f3bedf;
  --pink-soft:#f7d3ea;
  --ink:#1c1c1c;
  --grey:#6f6f6f;
  --grey-light:#a9a9a9;
  --hero-bg:#f4f4f4;
  --lavender:#f5ecfa;
  --white:#ffffff;
}
*{box-sizing:border-box;margin:0;padding:0}
html,body{width:1200px;height:3806px;overflow:hidden}
body{position:relative;font-family:"Poppins",sans-serif;color:var(--ink);background:var(--white)}
.abs{position:absolute}

/* Hero */
.hero{position:absolute;left:0;top:0;width:1200px;height:740px;background:var(--hero-bg);overflow:hidden}
.brand{position:absolute;left:48px;top:120px;display:flex;align-items:center;gap:14px}
.brand-dot{width:46px;height:46px;border-radius:50%;background:var(--teal)}
.brand-name{font-size:36px;font-weight:600;color:var(--magenta)}
.nav{position:absolute;top:84px;left:0;width:1200px;font-size:13px;font-weight:400;letter-spacing:.3px}
.nav a{position:absolute;color:var(--ink);text-decoration:none}
.btn-signin{position:absolute;left:1027px;top:69px;width:130px;height:45px;border-radius:23px;background:var(--magenta);color:var(--white);font-size:14px;font-weight:500;display:flex;align-items:center;justify-content:center}
.hero-blob{position:absolute;left:560px;top:145px}
.hero-photo{position:absolute;left:640px;top:150px;width:320px;height:530px;border-radius:160px 160px 40px 40px;background:linear-gradient(180deg,#8c8c8c,#d9d9d9)}
.hero-title{position:absolute;left:45px;top:372px;font-size:48px;font-weight:500;line-height:58px;letter-spacing:.5px}
.hero-title .hl{background:var(--teal);color:var(--white);padding:0 4px}
.hero-rule{position:absolute;left:387px;top:459px;width:192px;height:3px;background:var(--ink)}
.hero-text{position:absolute;left:48px;top:493px;width:500px;font-size:15.5px;line-height:25px}
.btn-shop{position:absolute;left:47px;top:575px;width:197px;height:50px;border-radius:25px;background:var(--teal);color:var(--white);font-size:15px;font-weight:500;display:flex;align-items:center;justify-content:center;box-shadow:0 6px 12px rgba(0,0,0,.15)}
.dots span{position:absolute;top:696px;width:12px;height:12px;border-radius:50%;background:#bdbdbd}
.dots span.on{background:var(--ink)}

/* Section heads */
.eyebrow{position:absolute;left:470px;width:260px;height:18px;font-size:10px;letter-spacing:2px;color:var(--grey);text-align:center;line-height:18px;background:linear-gradient(90deg,transparent,#f0f0f0 20%,#f0f0f0 80%,transparent)}
.sec-title{position:absolute;left:0;width:1200px;text-align:center;font-size:30px;font-weight:500}
.sec-title em{font-style:normal;color:var(--teal)}
.sec-sub{position:absolute;left:0;width:1200px;text-align:center;font-size:14px;line-height:17px;color:var(--grey);font-weight:300}

/* Services */
.blob-back{position:absolute;left:42px;top:937px;width:392px;height:360px;border-radius:50%;background:#e3f6f9;transform:rotate(-15deg)}
.blob-photo{position:absolute;left:48px;top:945px;width:375px;height:320px;border-radius:48% 52% 44% 56%/55% 45% 55% 45%;background:linear-gradient(160deg,var(--teal),#e6d8bf 70%)}
.service{position:absolute;display:flex;gap:20px}
.service-icon{width:82px;height:82px;border-radius:50%;background:var(--teal);flex:none;display:flex;align-items:center;justify-content:center}
.service h3{font-size:17px;font-weight:500;margin-top:12px}
.service p{font-size:10.5px;line-height:13px;color:var(--grey);margin-top:12px;width:210px}

/* About */
.about{position:absolute;left:0;top:1375px;width:1200px;height:515px;background:var(--pink);overflow:hidden}
.about-panel{position:absolute;left:0;top:155px;width:800px;height:317px;background:rgba(255,255,255,.25)}
.about-side{position:absolute;left:0;top:0}
.about-photo{position:absolute;left:860px;top:-20px;width:340px;height:535px;background:linear-gradient(180deg,#2a2a2a,#d9d9d9 85%)}
.about h2{position:absolute;left:48px;top:65px;font-size:47px;font-weight:600;color:#333}
.about h2 span{color:var(--white)}
.about-text{position:absolute;left:50px;top:157px;width:650px;font-size:15.3px;line-height:25.6px;color:#222}
.about-text p+p{margin-top:25.6px}

/* Pricing */
.card{position:absolute;width:251px;height:433px;border-radius:8px;background:var(--white);box-shadow:0 6px 22px rgba(0,0,0,.08);overflow:hidden;text-align:center}
.card-top{position:absolute;left:0;top:0}
.card .star{position:absolute;left:105px;top:22px}
.card h4{position:absolute;left:0;width:100%;top:70px;font-size:28px;font-weight:500;color:var(--teal)}
.card .price{position:absolute;left:0;width:100%;top:112px;font-size:38px;font-weight:700}
.card .price sup{font-size:20px;font-weight:500;vertical-align:16px}
.card .price small{font-size:22px;font-weight:400}
.card ul{position:absolute;left:18px;top:258px;list-style:none;text-align:left;font-size:15px;line-height:20px;color:var(--grey-light)}
.card li{position:relative;padding-left:20px;margin-bottom:6px;width:215px}
.card li::before{content:"";position:absolute;left:2px;top:4px;width:5px;height:9px;border:solid var(--magenta);border-width:0 2px 2px 0;transform:rotate(45deg)}
.card .btn{position:absolute;left:58px;top:373px;width:135px;height:44px;border-radius:22px;background:var(--teal);color:var(--white);font-size:16px;font-weight:500;display:flex;align-items:center;justify-content:center;box-shadow:0 5px 10px rgba(30,188,208,.35)}
.card.pro{background:linear-gradient(180deg,var(--teal-light),var(--teal-dark));color:var(--white)}
.card.pro h4{color:var(--ink);top:70px}
.card.pro .price{color:var(--white);top:115px}
.card.pro ul{top:258px;color:var(--white)}
.card.pro li::before{border-color:var(--magenta)}
.card.pro .btn{background:var(--white);color:var(--ink);top:372px}

/* Gallery */
.gallery{position:absolute;left:0;top:2683px;width:1200px;display:grid;grid-template-columns:repeat(5,240px);grid-auto-rows:232px}
.gallery div{border:1px solid rgba(255,255,255,.5)}

/* Footer */
.footer-wave{position:absolute;left:0;top:3150px}
.footer-brand{position:absolute;left:0;width:1200px;top:3500px;display:flex;justify-content:center;align-items:center;gap:14px}
.footer-brand .brand-name{color:var(--white);font-size:46px}
.footer-brand .brand-dot{background:var(--magenta);width:54px;height:54px}
.footer h5{position:absolute;font-size:22px;font-weight:700;color:#111}
.footer-links{position:absolute;left:48px;top:3608px;list-style:none;font-size:15.5px;line-height:26px;color:var(--white)}
.footer-contact{position:absolute;left:993px;top:3604px;font-size:15.5px;line-height:26px;color:var(--white)}
.footer-tag{position:absolute;left:370px;width:460px;top:3617px;text-align:center;font-size:12px;line-height:17px;font-weight:600;color:var(--white)}
.social{position:absolute;top:3677px;width:22px;height:22px;border-radius:50%;background:#111}
.copyright{position:absolute;left:0;width:1200px;top:3780px;text-align:center;font-size:11px;color:var(--white)}
</style>
</head>
<body>

<header class="hero">
  <div class="brand"><span class="brand-dot"></span><span class="brand-name">Brindle Hound</span></div>
  <nav class="nav">
    <a style="left:483px">HOME</a>
    <a style="left:561px">ABOUT</a>
    <a style="left:645px">SERVICES</a>
    <a style="left:746px">PHOTOS</a>
    <a style="left:839px">POLICIES</a>
    <a style="left:935px">CONTACT</a>
  </nav>
  <div class="btn-signin">SIGN IN</div>

  <svg class="hero-blob" width="640" height="560" viewBox="0 0 640 560" aria-hidden="true">
    <path d="M60 300 C20 160 110 10 290 5 C410 0 400 110 470 180 C560 270 520 470 370 520 C220 570 100 440 60 300Z" fill="var(--pink)"/>
    <path d="M520 60 L640 60 L640 520 L580 520 Z" fill="#e9e9e9"/>
  </svg>
  <div class="hero-photo" role="img" aria-label="Photo of a grey and white dog sitting, looking at the camera"></div>

  <h1 class="hero-title">THE <span class="hl">RIGHT</span> PLACE<br>FOR YOUR PET</h1>
  <div class="hero-rule"></div>
  <p class="hero-text">Lorem ipsum dolor sit amet, consectetur adipiscing elit, sed do eiusmod tempor incididunt ut labore et dolore magna aliqua.</p>
  <div class="btn-shop">SHOP NOW</div>
  <div class="dots"><span style="left:556px"></span><span style="left:581px"></span><span class="on" style="left:606px"></span><span style="left:631px"></span></div>
</header>

<section class="services">
  <div class="eyebrow" style="top:804px">WE CARE FOR YOUR PET</div>
  <h2 class="sec-title" style="top:823px">Welcome to <em>Brindle Hound!</em></h2>
  <p class="sec-sub" style="top:879px">We provide daycare for your pet to alleviate<br>loneliness and boredom</p>

  <div class="blob-back"></div>
  <div class="blob-photo" role="img" aria-label="Photo of a smiling golden retriever"></div>

  <div class="service" style="left:490px;top:1007px">
    <div class="service-icon">
      <svg width="44" height="44" viewBox="0 0 44 44" fill="none" stroke="#fff" stroke-width="2.5"><circle cx="12" cy="32" r="6"/><circle cx="32" cy="32" r="6"/><path d="M16 27 L34 6 M28 27 L10 6"/></svg>
    </div>
    <div><h3>Pet Grooming</h3><p>Our team of pet hair stylists is happy to make your animal look pretty and happy.</p></div>
  </div>
  <div class="service" style="left:844px;top:1007px">
    <div class="service-icon">
      <svg width="46" height="46" viewBox="0 0 46 46" fill="none" stroke="#fff" stroke-width="2.2"><circle cx="17" cy="17" r="11"/><path d="M17 10 V17 H23"/><rect x="14" y="31" width="26" height="7" rx="1"/><path d="M14 38 V42 M40 38 V42 M18 31 V27 H26 V31"/></svg>
    </div>
    <div><h3>Overnight Boarding</h3><p>Brindle Hound offers overnight boarding for dogs over 6 weeks of age.</p></div>
  </div>
  <div class="service" style="left:490px;top:1137px">
    <div class="service-icon">
      <svg width="44" height="44" viewBox="0 0 44 44" fill="#fff"><ellipse cx="22" cy="30" rx="9" ry="7"/><circle cx="10" cy="20" r="4"/><circle cx="17" cy="12" r="4"/><circle cx="27" cy="12" r="4"/><circle cx="34" cy="20" r="4"/></svg>
    </div>
    <div><h3>Doggie Daycare</h3><p>Socialization is an important part of raising a happy and healthy pup.</p></div>
  </div>
</section>

<section class="about">
  <svg class="about-side" width="1200" height="515" viewBox="0 0 1200 515" aria-hidden="true">
    <path d="M770 0 C700 120 690 360 780 515 L1200 515 L1200 0Z" fill="var(--magenta)"/>
  </svg>
  <div class="about-panel"></div>
  <div class="about-photo" role="img" aria-label="Photo of a black and white dog with its tongue out"></div>
  <h2>A Little Bit <span>About Us</span></h2>
  <div class="about-text">
    <p>Brindle Hound's mission is to provide gentle, loving care for your pets in a fun and friendly environment in a way that allows you, the pet owner to worry less about your companion while you are away. We want to create a stress free environment for our furry guests and a fun, playful atmosphere for our employees.</p>
    <p>A tired pup is a happy pup. That's why we have provided several indoor and outdoor play areas to stimulate your pup so he or she doesn't have time to miss you. You can rest assured your furbaby will have plenty of playful socialization throughout the day. We know how nervous pets can get when away from their humans and we want to ensure that the pet feels no anxiety during the separation.</p>
    <p>Marla Quint and Tessa Dorn, Owners</p>
  </div>
</section>

<section class="pricing">
  <div class="eyebrow" style="top:1962px">WE CARE FOR YOUR PET</div>
  <h2 class="sec-title" style="top:1982px">Daycare Subscription to <em>Brindle Hound!</em></h2>
  <p class="sec-sub" style="top:2036px">We provide daycare for your pet to alleviate<br>loneliness and boredom</p>

  <div class="card" style="left:238px;top:2165px">
    <svg class="card-top" width="251" height="240" aria-hidden="true"><path d="M0 0 H225 L251 165 L0 238Z" fill="var(--lavender)"/></svg>
    <svg class="star" width="42" height="42" viewBox="0 0 24 24"><path d="M12 2l3 6.5 7 .8-5.2 4.8 1.4 7L12 17.6 5.8 21.1l1.4-7L2 9.3l7-.8z" fill="#d8d3dc"/></svg>
    <h4>Starter</h4>
    <div class="price"><sup>$</sup>150<small>/mo</small></div>
    <ul><li>4 hair styles</li><li>one week Overnight Boarding</li><li>15 Days Doggie Daycare</li></ul>
    <div class="btn">Sign Up</div>
  </div>

  <div class="card" style="left:733px;top:2165px">
    <svg class="card-top" width="251" height="240" aria-hidden="true"><path d="M0 0 H225 L251 165 L0 238Z" fill="var(--lavender)"/></svg>
    <svg class="star" width="42" height="42" viewBox="0 0 24 24"><path d="M12 2l3 6.5 7 .8-5.2 4.8 1.4 7L12 17.6 5.8 21.1l1.4-7L2 9.3l7-.8z" fill="#d8d3dc"/></svg>
    <h4>Premium</h4>
    <div class="price"><sup>$</sup>400<small>/mo</small></div>
    <ul><li>4 hair styles</li><li>one week Overnight Boarding</li><li>15 Days Doggie Daycare</li></ul>
    <div class="btn">Sign Up</div>
  </div>

  <div class="card pro" style="left:485px;top:2105px;height:434px">
    <svg class="card-top" width="251" height="240" aria-hidden="true"><path d="M0 0 H205 L240 160 L0 240Z" fill="var(--teal-light)" opacity=".9"/></svg>
    <svg class="star" width="46" height="46" viewBox="0 0 24 24"><path d="M12 2l3 6.5 7 .8-5.2 4.8 1.4 7L12 17.6 5.8 21.1l1.4-7L2 9.3l7-.8z" fill="#fff"/></svg>
    <h4>Professional</h4>
    <div class="price"><sup>$</sup>250<small>/mo</small></div>
    <ul><li>4 hair styles</li><li>one week Overnight Boarding</li><li>15 Days Doggie Daycare</li></ul>
    <div class="btn">Sign Up</div>
  </div>
</section>

<section class="gallery" aria-label="Photo gallery">
  <div role="img" aria-label="Photo of a small white terrier on a floor" style="background:linear-gradient(160deg,#b98a5a,#e6ddd0)"></div>
  <div role="img" aria-label="Photo of a doodle walking on grass" style="background:linear-gradient(160deg,#8a7a5a,#5f8a3a)"></div>
  <div role="img" aria-label="Photo of a tricolour terrier close up" style="background:linear-gradient(160deg,#1f2f45,#c79a68)"></div>
  <div role="img" aria-label="Photo of a dalmatian greeting a woman" style="background:linear-gradient(160deg,#c56a4a,#e8d3c1)"></div>
  <div role="img" aria-label="Photo of a happy golden retriever" style="background:linear-gradient(160deg,#2c2c2c,#c98a3e)"></div>
  <div role="img" aria-label="Photo of a terrier under a table" style="background:linear-gradient(160deg,#6a4d3b,#d9d0c7)"></div>
  <div role="img" aria-label="Photo of a white poodle on a striped chair" style="background:linear-gradient(160deg,#5a6677,#e9e4dc)"></div>
  <div role="img" aria-label="Photo of a husky lying down" style="background:linear-gradient(160deg,#2a2420,#8d7866)"></div>
  <div role="img" aria-label="Photo of a woman hugging a dalmatian" style="background:linear-gradient(160deg,#d98a8f,#5a3a2a)"></div>
  <div role="img" aria-label="Photo of a doodle running on grass" style="background:linear-gradient(160deg,#3f3a30,#8e9a5a)"></div>
  <div role="img" aria-label="Photo of a brown vizsla in a car" style="background:linear-gradient(160deg,#2a1a14,#9a4a2a)"></div>
  <div role="img" aria-label="Photo of a black and white dog standing by a person" style="background:linear-gradient(160deg,#3d5a2a,#3a4b6a)"></div>
  <div role="img" aria-label="Photo of a small white dog with a flower collar" style="background:linear-gradient(160deg,#f2f0ee,#c9c2bb)"></div>
  <div role="img" aria-label="Photo of a tricolour terrier outdoors" style="background:linear-gradient(160deg,#1f2f45,#b58a60)"></div>
  <div role="img" aria-label="Photo of a dog in a dim room" style="background:linear-gradient(160deg,#1a1a1a,#4a3a30)"></div>
</section>

<footer class="footer">
  <svg class="footer-wave" width="1200" height="656" viewBox="0 0 1200 656" aria-hidden="true">
    <path d="M0 40 C120 150 320 200 560 180 C780 160 900 100 1040 90 C1110 85 1170 100 1200 120 L1200 656 L0 656Z" fill="#5fd6e6"/>
    <path d="M0 110 C160 220 380 230 580 200 C800 165 920 110 1060 100 C1130 96 1180 110 1200 125 L1200 656 L0 656Z" fill="var(--teal)"/>
    <path d="M230 656 C420 590 700 540 930 530 L1040 656Z" fill="#111"/>
  </svg>
  <div class="footer-brand"><span class="brand-dot"></span><span class="brand-name">Brindle Hound</span></div>
  <h5 style="left:48px;top:3564px">QUICK LINKS</h5>
  <ul class="footer-links"><li>Home</li><li>Locations</li><li>Seasonal Menu</li><li>Story</li><li>Catering</li><li>Blog</li></ul>
  <p class="footer-tag">Fernwell Labs is dedicated to providing modern tools to the agriculture industry, one greenhouse at a time.</p>
  <span class="social" style="left:465px" aria-label="Social link"></span>
  <span class="social" style="left:546px" aria-label="Social link"></span>
  <span class="social" style="left:629px" aria-label="Social link"></span>
  <span class="social" style="left:710px" aria-label="Social link"></span>
  <h5 style="left:993px;top:3564px">CONTACT US</h5>
  <div class="footer-contact">418 Larkspur Ave.<br>Bellmont, CA 90512<br>-<br>T: 555.210.4832<br>F: 555.210.4900</div>
  <p class="copyright">© 2020 BRINDLEHOUND</p>
</footer>

</body>
</html>
```